Flyer Design Print Ad for Clothing Store

We are a modest women's clothing store. We are looking for a print ad 90*134 mm that is attention grabbing and can serve as a template for us going forward. We cannot use pictures of actual women. We need it to include our logo, store hours, physical address, website, phone number. We would use this template and change the call to action as necessary e. g. BOGO Sale, 30% off, flash sale, summer sale etc. Our colors are black and white and our fonts are Bodoni sans and Athens.

Target Market(s)

Women from teen to age 70

Industry/Entity Type

Women's clothing

Font styles to use
Other font styles liked:
• Athens, Bodoni Sans

Requirements
Must have
• Our, logo, phone number, website, address and store hours
Nice to have
• I'd like something that's not just our flat logo but something that will make someone pause to look
Should not have
• Pictures of women

```html
<!DOCTYPE html>
<html lang="en">
<head>
<meta charset="utf-8">
<title>Lumerah – BOGO Sale Flyer</title>
<link rel="stylesheet" href="https://fonts.googleapis.com/css2?family=Bodoni+Moda:wght@600;700&family=Marcellus&display=swap">
<style>
  :root {
    --ink: #2b2b2b;
    --paper: #f7f7f7;
    --backdrop: #e6e6e6;
    --white: #ffffff;
    --art-a: #d98a7a;
    --art-b: #f2c3a8;
    --art-c: #5a5e70;
  }
  * { margin: 0; padding: 0; box-sizing: border-box; }
  html, body { width: 1200px; height: 1200px; overflow: hidden; background: var(--backdrop); }
  .flyer {
    position: absolute; left: 242px; top: 67px;
    width: 716px; height: 1065px;
    background: var(--paper);
    color: var(--ink);
    font-family: "Marcellus", serif;
    overflow: hidden;
  }
  .brand-disc {
    position: absolute; left: 265px; top: 25px;
    width: 174px; height: 174px; border-radius: 50%;
    background: var(--ink);
  }
  .brand-name {
    position: absolute; left: 0; width: 716px; top: 226px;
    text-align: center; font-weight: 400; font-size: 50px;
    letter-spacing: 15px; text-indent: 15px; line-height: 54px;
  }
  .illustration {
    position: absolute; left: 133px; top: 306px; width: 451px; height: 335px;
    border-radius: 40px;
    background: linear-gradient(100deg, var(--art-a) 0%, var(--art-b) 50%, var(--art-c) 100%);
    opacity: 0.55;
  }
  .headline { position: absolute; left: 0; top: 0; }
  .headline-bogo { font-family: "Bodoni Moda", serif; font-weight: 700; fill: var(--ink); }
  .headline-sale { font-family: "Bodoni Moda", serif; font-weight: 600; fill: var(--white); }
  .offer { font-family: "Marcellus", serif; fill: var(--ink); stroke: var(--ink); stroke-width: 1.5; }
  .contact-list { position: absolute; left: 53px; top: 926px; list-style: none; }
  .contact-item { display: flex; align-items: center; height: 39px; font-size: 22px; }
  .contact-icon { width: 29px; height: 29px; margin-right: 11px; flex: none; }
  .hours {
    position: absolute; left: 425px; top: 931px; width: 236px; height: 106px;
    background: var(--ink); color: var(--white); text-align: center;
  }
  .hours-title { height: 24px; line-height: 24px; font-size: 16px; border-bottom: 1.5px solid var(--white); }
  .hours-days { font-size: 21px; line-height: 26px; margin-top: 2px; white-space: nowrap; }
  .hours-time { font-size: 21px; line-height: 26px; }
</style>
</head>
<body>
<main class="flyer">
  <div class="brand-disc"></div>
  <h1 class="brand-name">LUMERAH</h1>

  <div class="illustration" role="img" aria-label="Line-art fashion illustration of three stylish figures in hats and flowing outfits"></div>

  <svg class="headline" width="716" height="900" aria-label="BOGO SALE 30% OFF">
    <text class="headline-bogo" x="53" y="759" font-size="120" textLength="304" lengthAdjust="spacingAndGlyphs">BOGO</text>
    <rect x="381" y="675" width="282" height="81" fill="var(--ink)"/>
    <text class="headline-sale" x="401" y="750" font-size="98" textLength="239" lengthAdjust="spacingAndGlyphs">SALE</text>
    <polyline points="60,767 60,838 148,838" fill="none" stroke="var(--ink)" stroke-width="2"/>
    <polyline points="655,767 655,838 562,838" fill="none" stroke="var(--ink)" stroke-width="2"/>
    <text class="offer" x="168" y="874" font-size="100" textLength="378" lengthAdjust="spacingAndGlyphs">30% OFF</text>
  </svg>

  <ul class="contact-list">
    <li class="contact-item">
      <svg class="contact-icon" viewBox="0 0 32 32" aria-hidden="true">
        <circle cx="16" cy="16" r="16" fill="var(--ink)"/>
        <path d="M11 8c1-1 2-1 3 0l2 3c.6 1 .3 2-.5 2.6l-1 .8c.8 2 2.2 3.4 4 4.3l.9-1c.7-.8 1.7-1 2.6-.4l3 2c1 .7 1 1.8 0 2.8-2 2-4 2-7 0-3-2-6-5-8-8-1.5-3-1.5-5 1-7z" fill="var(--white)"/>
      </svg>
      <span>123-456-7890</span>
    </li>
    <li class="contact-item">
      <svg class="contact-icon" viewBox="0 0 32 32" aria-hidden="true">
        <circle cx="16" cy="16" r="16" fill="var(--ink)"/>
        <g fill="none" stroke="var(--white)" stroke-width="1.5">
          <circle cx="16" cy="16" r="10"/>
          <ellipse cx="16" cy="16" rx="4.5" ry="10"/>
          <line x1="6" y1="16" x2="26" y2="16"/>
          <path d="M8 11h16M8 21h16"/>
        </g>
      </svg>
      <span>yourwebsiet.com</span>
    </li>
    <li class="contact-item">
      <svg class="contact-icon" viewBox="0 0 32 32" aria-hidden="true">
        <circle cx="16" cy="16" r="16" fill="var(--ink)"/>
        <path d="M16 6c-4 0-7 3-7 7 0 5 7 12 7 12s7-7 7-12c0-4-3-7-7-7z" fill="none" stroke="var(--white)" stroke-width="1.8"/>
        <circle cx="16" cy="13" r="2.6" fill="var(--white)"/>
      </svg>
      <span>Cedar Grove Shopping Center</span>
    </li>
  </ul>

  <section class="hours">
    <div class="hours-title">WORKING HOURS</div>
    <div class="hours-days">SUNDAY - THURSDAY</div>
    <div class="hours-time">10:30-12:30</div>
    <div class="hours-time">20:30 - 22:30</div>
  </section>
</main>
</body>
</html>
```